Business card design needed

A business card and logo for my energy healing practice Fernvale Stillwater. It should match my website www.fernvalestillwater-example.com in colours and atmosphere. It should look at bit rustic in combination with nature linking in with the natural healing techniques I offer in a heritage country town in NSW Australia. My business also includes a directory of other health and healing practitioners 'The Spring'. It would be nice if a graphic impression of the attached picture of the water feature in my front yard can be used.

Industry/Entity Type

Health

Contact Information for Business Card

Fernvale Stillwater, Delphine Ashcroft, 14 Larchfield St, Merrigal NSW 2699, M. 0491 363 718, info@fernvalestillwater-example.com, www.fernvalestillwater-example.com,
Gentle Energy Work - Rooted in Country Calm
Facebook/Twitter see Capital Renewal

```html
<!DOCTYPE html>
<html lang="en">
<head>
<meta charset="utf-8">
<title>Fernvale Stillwater – Business Card</title>
<link rel="stylesheet" href="https://fonts.googleapis.com/css2?family=Cormorant+Garamond:wght@600&family=Open+Sans:wght@400;700&display=swap">
<style>
  :root {
    --backdrop: #8a8a8a;
    --slate-dark: #1f2a2a;
    --slate-mid: #4a5756;
    --mist: #d9dcdc;
    --mist-light: #eef0ef;
    --band: #2b2b2b;
    --ink: #2a2a2a;
    --ink-soft: #3d3d3d;
    --icon: #3a3a3a;
    --white: #ffffff;
    --garden-green: #5d6b4f;
    --garden-gravel: #a8977c;
    --garden-soil: #7d6c55;
  }
  html, body {
    margin: 0;
    width: 1200px;
    height: 861px;
    overflow: hidden;
    background: var(--backdrop);
  }
  .stage {
    position: relative;
    width: 1200px;
    height: 861px;
  }
  .card {
    position: absolute;
    top: 272px;
    width: 520px;
    height: 316px;
    overflow: hidden;
    box-shadow: 0 6px 18px rgba(0, 0, 0, 0.35);
  }
  .card--front { left: 60px; }
  .card--back  { left: 620px; background: var(--mist-light); }

  /* Front */
  .garden-photo {
    position: absolute;
    inset: 0;
    background: linear-gradient(180deg, var(--slate-dark) 0%, var(--slate-mid) 32%, var(--garden-green) 55%, var(--garden-gravel) 80%, var(--garden-soil) 100%);
  }
  .front-wordmark {
    position: absolute;
    top: 40px;
    left: 0;
    right: 0;
    margin: 0;
    text-align: center;
    font-family: "Cormorant Garamond", serif;
    font-weight: 600;
    font-size: 46px;
    letter-spacing: 1px;
    color: var(--white);
  }

  /* Back */
  .mist-photo {
    position: absolute;
    left: 0; right: 0; top: 0;
    height: 262px;
    background: linear-gradient(180deg, var(--slate-dark) 0%, var(--slate-mid) 24%, var(--mist) 48%, var(--mist-light) 100%);
  }
  .back-wordmark {
    position: absolute;
    top: 20px;
    left: 24px;
    margin: 0;
    font-family: "Cormorant Garamond", serif;
    font-weight: 600;
    font-size: 34px;
    letter-spacing: 1px;
    color: var(--white);
  }
  .contact-list {
    position: absolute;
    top: 96px;
    left: 18px;
    margin: 0;
    padding: 0;
    list-style: none;
    font-family: "Open Sans", sans-serif;
    font-size: 11.5px;
    color: var(--ink-soft);
  }
  .contact-list li {
    display: flex;
    align-items: center;
    gap: 7px;
    height: 19px;
  }
  .contact-icon {
    width: 14px;
    height: 14px;
    flex: none;
  }
  .holder-name {
    position: absolute;
    right: 28px;
    top: 206px;
    margin: 0;
    font-family: "Open Sans", sans-serif;
    font-weight: 700;
    font-size: 24px;
    color: var(--ink);
  }
  .tagline-band {
    position: absolute;
    left: 0; right: 0; bottom: 0;
    height: 54px;
    background: var(--band);
    display: flex;
    align-items: center;
    justify-content: center;
  }
  .tagline {
    margin: 0;
    font-family: "Cormorant Garamond", serif;
    font-weight: 600;
    font-size: 19px;
    color: var(--white);
  }
</style>
</head>
<body>
<main class="stage">

  <section class="card card--front">
    <div class="garden-photo" role="img" aria-label="Garden with a water feature in a circular brick-edged flower bed on gravel, misty trees behind"></div>
    <h1 class="front-wordmark">Fernvale Stillwater</h1>
  </section>

  <section class="card card--back">
    <div class="mist-photo" role="img" aria-label="Misty winter garden with bare trees and a frosted lawn"></div>
    <h2 class="back-wordmark">Fernvale Stillwater</h2>

    <ul class="contact-list">
      <li>
        <svg class="contact-icon" viewBox="0 0 14 14"><circle cx="7" cy="7" r="7" fill="var(--icon)"/><path d="M7 3a2.4 2.4 0 0 0-2.4 2.4C4.6 7.2 7 10.5 7 10.5s2.4-3.3 2.4-5.1A2.4 2.4 0 0 0 7 3zm0 3.3a.9.9 0 1 1 0-1.8.9.9 0 0 1 0 1.8z" fill="#fff"/></svg>
        14 Larchfield St, Merrigal NSW 2699
      </li>
      <li>
        <svg class="contact-icon" viewBox="0 0 14 14"><circle cx="7" cy="7" r="7" fill="var(--icon)"/><path d="M4.6 3.6l1.3-.3.7 1.6-.8.6a4.6 4.6 0 0 0 2.1 2.1l.6-.8 1.6.7-.3 1.3C7 9.2 4.4 6.6 4.6 3.6z" fill="#fff"/></svg>
        0491 363 718
      </li>
      <li>
        <svg class="contact-icon" viewBox="0 0 14 14"><circle cx="7" cy="7" r="7" fill="var(--icon)"/><rect x="3.5" y="4.5" width="7" height="5" fill="none" stroke="#fff" stroke-width="1"/><path d="M3.5 4.5L7 7.3l3.5-2.8" fill="none" stroke="#fff" stroke-width="1"/></svg>
        info@fernvalestillwater-example.com
      </li>
      <li>
        <svg class="contact-icon" viewBox="0 0 14 14"><circle cx="7" cy="7" r="7" fill="var(--icon)"/><circle cx="7" cy="7" r="3.6" fill="none" stroke="#fff" stroke-width="0.9"/><path d="M3.4 7h7.2M7 3.4c-1.6 2-1.6 5.2 0 7.2M7 3.4c1.6 2 1.6 5.2 0 7.2" fill="none" stroke="#fff" stroke-width="0.8"/></svg>
        www.fernvalestillwater-example.com
      </li>
      <li>
        <svg class="contact-icon" viewBox="0 0 14 14"><circle cx="7" cy="7" r="7" fill="var(--icon)"/></svg>
        Capital Renewal
      </li>
      <li>
        <svg class="contact-icon" viewBox="0 0 14 14"><circle cx="7" cy="7" r="7" fill="var(--icon)"/></svg>
        Capital Renewal
      </li>
    </ul>

    <p class="holder-name">Delphine Ashcroft</p>

    <div class="tagline-band">
      <p class="tagline">Gentle Energy Work - Rooted in Country Calm</p>
    </div>
  </section>

</main>
</body>
</html>
```